International Parcel Forwarder needs website redesign and logo

We need an updated website design to make our existing site look more modern, global and trustworthy. Current site
www.parvento.com -- we do not want to rebuild headers or at this point do copyright we are simply looking to make the site pop:)
The service we provide is for shoppers living outside the USA looking to shop here and save money on shipping or get access to stores that won't ship internationally or accept international payment.
Target Market(s)
Online shoppers living outside the USA
Industry/Entity Type
Shipping
Logo Text
US shopping, global shipping
Coding
Coded - Design and coding required
Number of Pages Required
5+ page
Font styles to use

```html
<!DOCTYPE html>
<html lang="en">
<head>
<meta charset="utf-8">
<title>Parvento — Shop At Any U.S. Retailer. Ship Anywhere.</title>
<link rel="stylesheet" href="https://fonts.googleapis.com/css2?family=Lato:wght@400;700;900&family=Open+Sans:wght@400;600;700&display=swap">
<style>
:root{
  --navy:#1d2833;
  --brand:#2a8fd8;
  --blue:#1a6fc0;
  --blue-soft:#4b9fd9;
  --orange:#f29a2e;
  --ink:#1f1f1f;
  --muted:#8a8a8a;
  --panel:#f3f3f3;
  --rule:#dcdcdc;
  --footer:#4a9fd8;
  --bottom:#2a2a2a;
}
*{box-sizing:border-box;margin:0;padding:0}
html,body{width:1200px;height:3103px;overflow:hidden}
body{position:relative;background:#fff;font-family:"Open Sans",Arial,sans-serif;color:var(--ink)}
section,header,footer{position:absolute;left:0;width:1200px}

/* header */
.site-header{top:0;height:132px;background:var(--navy)}
.logo{position:absolute;left:103px;top:35px;display:flex;align-items:center;gap:12px}
.logo-name{font-family:"Lato",sans-serif;font-size:58px;color:var(--brand);line-height:1}
.auth{position:absolute;top:25px;right:110px;display:flex;gap:14px}
.auth a{display:block;height:27px;line-height:27px;padding:0 16px;font:700 11px "Open Sans",sans-serif;color:#fff;text-decoration:none;letter-spacing:.5px}
.auth .login{background:var(--orange);width:85px}
.auth .signup{background:var(--blue-soft);width:95px}
.main-nav{position:absolute;top:80px;right:108px;display:flex;gap:30px}
.main-nav a{font:600 14px "Open Sans",sans-serif;color:#fff;text-decoration:none}

/* hero */
.hero{top:132px;height:420px;background:linear-gradient(180deg,#7fb6e4 0%,#b8d8ef 38%,#5a90c4 62%,#1e4f86 80%,#163c6a 100%)}
.hero-photo{position:absolute;inset:0}
.hero-copy{position:absolute;left:103px;top:130px;color:#fff}
.hero-kicker{font:400 24px "Lato",sans-serif}
.hero-title{font:700 34px "Lato",sans-serif;margin-top:6px}
.hero-text{font:400 15px "Lato",sans-serif;line-height:21px;margin-top:16px;width:340px}
.hero-btn{display:block;width:145px;height:38px;line-height:38px;text-align:center;background:#2e86c9;color:#fff;font:400 14px "Lato",sans-serif;margin-top:26px;margin-left:-4px;text-decoration:none}
.slider-dots{position:absolute;top:578px;left:552px;display:flex;gap:17px}
.slider-dots span{width:14px;height:14px;border-radius:50%;background:var(--blue-soft)}
.slider-dots span:first-child{background:#1c1c1c}

/* section titles */
.section-title{position:absolute;left:0;width:1200px;text-align:center;font:700 28px "Lato",sans-serif;letter-spacing:1px;color:#151515}
.section-sub{position:absolute;left:0;width:1200px;text-align:center;font:400 12px "Open Sans",sans-serif;line-height:21px;color:var(--muted)}

/* steps */
.step{position:absolute;display:flex;gap:18px;align-items:flex-start}
.step svg{flex:none}
.step h3{font:700 16px "Lato",sans-serif;letter-spacing:.5px;color:#151515}
.step p{font:400 12.5px "Open Sans",sans-serif;line-height:17px;color:#333;margin-top:6px;width:250px}
.step ul{list-style:none;margin-top:6px}
.step li{position:relative;padding-left:22px;font:400 12.5px "Open Sans",sans-serif;line-height:17px;color:#333;width:280px}
.step li::before{content:"";position:absolute;left:3px;top:6px;width:7px;height:7px;border-radius:50%;background:#111}

/* video */
.video-band{top:1127px;height:518px;background:linear-gradient(180deg,#f1f2f4 0%,#e6e8eb 100%)}
.video-frame{position:absolute;left:141px;top:90px;width:918px;height:393px;background:#0b0b0b}
.video-art{position:absolute;left:132px;top:12px;width:648px;height:333px;background:linear-gradient(135deg,#7cc6ea 0%,#3a9fd8 50%,#1f86c9 100%)}
.video-brand{position:absolute;left:36px;top:40px;width:70px;height:60px;background:#1a1a1a}
.video-side{position:absolute;right:14px;top:20px;display:flex;flex-direction:column;gap:10px}
.video-side span{width:24px;height:22px;background:#2a2a2a;border-radius:3px}
.video-controls{position:absolute;left:24px;right:24px;bottom:12px;height:26px;display:flex;align-items:center;gap:12px}
.video-play{width:36px;height:24px;background:#1b1b1b;display:flex;align-items:center;justify-content:center}
.video-progress{flex:1;height:8px;background:#4a4a4a}
.video-hd{font:700 11px "Open Sans",sans-serif;color:#fff}

/* packing + calculator */
.tools{top:2166px;height:451px;background:var(--panel)}
.tools h2{position:absolute;font:700 27px "Lato",sans-serif;letter-spacing:1.5px;color:var(--blue)}
.tools-intro{position:absolute;left:103px;top:141px;width:470px;font:400 14px "Open Sans",sans-serif;line-height:31px;color:#444}
.tools-list{position:absolute;left:103px;top:204px;list-style:none}
.tools-list li{position:relative;padding-left:16px;font:400 13px "Open Sans",sans-serif;line-height:28px;color:#555}
.tools-list li::before{content:"";position:absolute;left:0;top:12px;width:5px;height:5px;border-radius:50%;background:var(--blue)}
.field-label{position:absolute;font:400 11px "Open Sans",sans-serif;color:#333}
.radio{position:absolute;display:flex;align-items:center;gap:8px;font:400 11px "Open Sans",sans-serif;color:#666}
.radio i{width:8px;height:8px;border-radius:50%;border:1px solid #bbb;background:#fff}
.radio i.on{background:#1b2f6a;border-color:#1b2f6a}
.input{position:absolute;background:#fff;border:1px solid #e2e2e2;font:400 11px "Open Sans",sans-serif;color:#999;padding:0 10px;display:flex;align-items:center}
.input.filled{background:#ececec;color:#444}
.calc-btn{position:absolute;left:910px;top:309px;width:129px;height:33px;background:var(--orange);color:#fff;font:600 12px "Open Sans",sans-serif;display:flex;align-items:center;justify-content:center;letter-spacing:.5px}
.note{position:absolute;left:910px;top:232px;font:400 10px "Open Sans",sans-serif;color:#555}

/* clients */
.clients{top:2632px;height:124px;background:#fff}
.clients-label{position:absolute;left:0;top:0;width:393px;height:124px;background:#ececec;clip-path:polygon(0 0,320px 0,393px 124px,0 124px)}
.clients-label span{position:absolute;left:95px;top:44px;font:400 29px "Lato",sans-serif;letter-spacing:1.5px;color:#222}
.client{position:absolute;top:42px;font:700 32px "Lato",sans-serif;line-height:40px;color:#222;white-space:nowrap}
.arrow{position:absolute;top:45px}

/* footer */
.site-footer{top:2756px;height:275px;background:var(--footer);color:#fff}
.footer-col{position:absolute;top:74px}
.footer-col h4{font:700 20px "Lato",sans-serif;letter-spacing:1px;margin-bottom:10px}
.footer-col p,.footer-col a{display:block;font:600 13px "Open Sans",sans-serif;line-height:27px;color:#fff;text-decoration:none;letter-spacing:.3px}
.footer-col .partner{font:700 20px "Lato",sans-serif;line-height:38px}
.footer-logo{position:absolute;left:52px;top:60px;display:flex;align-items:center;gap:8px}
.footer-logo span{font:400 36px "Lato",sans-serif}
.bottom-bar{position:absolute;left:0;top:3031px;width:1200px;height:72px;background:var(--bottom);color:#fff;text-align:center;font:600 13px "Open Sans",sans-serif;line-height:72px;letter-spacing:.5px}
</style>
</head>
<body>

<header class="site-header">
  <div class="logo">
    <svg width="71" height="71" viewBox="0 0 71 71" aria-hidden="true"><circle cx="35.5" cy="35.5" r="32" fill="none" stroke="#2a8fd8" stroke-width="4"/><circle cx="35.5" cy="35.5" r="20" fill="#2a8fd8"/></svg>
    <span class="logo-name">Parvento</span>
  </div>
  <div class="auth">
    <a class="login" href="#">LOG IN &#9656;</a>
    <a class="signup" href="#">SIGN UP &#8673;</a>
  </div>
  <nav class="main-nav">
    <a href="#">Shipping Calculator</a>
    <a href="#">How it Works</a>
    <a href="#">Parvento Pricing</a>
    <a href="#">Contact Us</a>
    <a href="#">Lean More</a>
    <a href="#">Blog</a>
  </nav>
</header>

<section class="hero">
  <div class="hero-photo" role="img" aria-label="Container cargo ship sailing on open sea under a bright cloudy sky"></div>
  <div class="hero-copy">
    <p class="hero-kicker">Shop At Any U.S.</p>
    <h1 class="hero-title">Retailer. Ship Anywhere.</h1>
    <p class="hero-text">Lorem Ipsum is simply dummy text of the printing and typesetting industry.</p>
    <a class="hero-btn" href="#">Learn More</a>
  </div>
</section>
<div class="slider-dots"><span></span><span></span><span></span><span></span></div>

<h2 class="section-title" style="top:650px">HOW PARVENTO WORKS</h2>
<p class="section-sub" style="top:693px">Lorem ipsum dolor sit amet, consectetuer adipiscing elit. Dolor sit amet, consectetuer adipiscing elit<br>lorem ipsum dolor sit amet, consectetuer adipiscing elit</p>

<div class="step" style="left:196px;top:780px">
  <svg width="84" height="64" viewBox="0 0 84 64" aria-hidden="true"><g fill="#1a6fc0"><rect x="0" y="4" width="30" height="22"/><rect x="32" y="6" width="40" height="5"/><rect x="32" y="16" width="40" height="5"/><rect x="0" y="28" width="66" height="5"/><rect x="0" y="38" width="60" height="5"/><rect x="0" y="48" width="46" height="5"/><path d="M52 58 L78 30 L84 36 L58 64 L50 64 Z"/></g></svg>
  <div><h3>LOREM IPSUM IS SIMPLY</h3><p>Register for your free U.S. shopping address</p></div>
</div>
<div class="step" style="left:668px;top:780px">
  <svg width="92" height="64" viewBox="0 0 92 64" aria-hidden="true"><g fill="none" stroke="#1a6fc0" stroke-width="4" stroke-linejoin="round"><path d="M18 24 L18 60 L74 60 L74 24"/><path d="M18 24 L46 34 L74 24"/><path d="M46 34 L46 60"/><path d="M18 24 L4 12 L32 4 L46 16 L60 4 L88 12 L74 24"/></g></svg>
  <div><h3>LOREM IPSUM IS SIMPLY</h3><p>Parvento receives your package and you get notified automatically</p></div>
</div>
<div class="step" style="left:196px;top:930px">
  <svg width="84" height="64" viewBox="0 0 84 64" aria-hidden="true"><g fill="#1a6fc0"><path d="M4 6 H80 L84 22 H0 Z"/><rect x="6" y="26" width="72" height="34"/></g><rect x="18" y="34" width="48" height="14" fill="#fff"/><rect x="4" y="58" width="76" height="4" fill="#1a6fc0"/></svg>
  <div><h3>LOREM IPSUM IS SIMPLY</h3><p>Shop anywhere in the U.S</p></div>
</div>
<div class="step" style="left:668px;top:930px">
  <svg width="92" height="64" viewBox="0 0 92 64" aria-hidden="true"><g fill="none" stroke="#1a6fc0" stroke-width="4"><circle cx="46" cy="32" r="24"/><ellipse cx="46" cy="32" rx="11" ry="24"/><path d="M22 32 H70"/><path d="M4 40 C20 60 72 60 88 24"/></g><path d="M80 14 L90 18 L84 26 Z" fill="#1a6fc0"/></svg>
  <div><h3>LOREM IPSUM IS SIMPLY</h3><p>You choose how to ship your package anywhere in the world</p></div>
</div>

<section class="video-band">
  <h2 class="section-title" style="top:38px">HOW PARVENTO WORKS</h2>
  <div class="video-frame">
    <div class="video-brand" role="img" aria-label="Video intro mark"></div>
    <div class="video-art" role="img" aria-label="Animated explainer of four cartoon shoppers dreaming of goods from U.S. stores"></div>
    <div class="video-side"><span></span><span></span><span></span></div>
    <div class="video-controls">
      <div class="video-play"><svg width="12" height="14" viewBox="0 0 12 14" aria-hidden="true"><path d="M0 0 L12 7 L0 14 Z" fill="#fff"/></svg></div>
      <div class="video-progress"></div>
      <span class="video-hd">HD</span>
    </div>
  </div>
</section>

<h2 class="section-title" style="top:1718px">HOW PARVENTO WORKS</h2>
<p class="section-sub" style="top:1763px">Lorem ipsum dolor sit amet, consectetuer adipiscing elit. Dolor sit amet, consectetuer adipiscing elit<br>lorem ipsum dolor sit amet, consectetuer adipiscing elit</p>

<div class="step" style="left:196px;top:1856px">
  <svg width="63" height="63" viewBox="0 0 63 63" aria-hidden="true"><circle cx="31.5" cy="31.5" r="29" fill="none" stroke="#1a6fc0" stroke-width="4"/><g fill="#1a6fc0"><circle cx="31.5" cy="22" r="6"/><path d="M21 42 a10.5 10 0 0 1 21 0 Z"/><circle cx="17" cy="28" r="4.5"/><path d="M9 44 a8 8 0 0 1 14 -6 V44 Z"/><circle cx="46" cy="28" r="4.5"/><path d="M40 38 a8 8 0 0 1 14 6 H40 Z"/></g></svg>
  <div><h3>EXPERIENCE</h3><ul><li>30 years experience in international shipping.</li><li>Excellent customer service</li></ul></div>
</div>
<div class="step" style="left:658px;top:1856px">
  <svg width="78" height="58" viewBox="0 0 78 58" aria-hidden="true"><g fill="#1a6fc0"><rect x="0" y="30" width="10" height="26"/><rect x="14" y="22" width="10" height="34"/><rect x="28" y="34" width="10" height="22"/><rect x="60" y="38" width="10" height="18"/></g><circle cx="50" cy="20" r="17" fill="none" stroke="#1a6fc0" stroke-width="4"/><text x="50" y="27" text-anchor="middle" font-family="Lato, sans-serif" font-weight="700" font-size="20" fill="#1a6fc0">$</text><path d="M62 32 L74 46" stroke="#1a6fc0" stroke-width="5"/></svg>
  <div><h3>VALUE</h3><ul><li>Discounted shipping rates with major carriers</li><li>No membership or joining fees</li><li>Low consolidation feesy</li></ul></div>
</div>
<div class="step" style="left:196px;top:2007px">
  <svg width="66" height="60" viewBox="0 0 66 60" aria-hidden="true"><path d="M33 56 L8 32 A14 14 0 0 1 33 12 A14 14 0 0 1 58 32 Z" fill="none" stroke="#1a6fc0" stroke-width="4" stroke-linejoin="round"/><path d="M14 34 L26 24 L38 32 L48 26 M22 40 L32 34 M28 46 L38 38" fill="none" stroke="#1a6fc0" stroke-width="4" stroke-linecap="round"/></svg>
  <div><h3>TRUST</h3><ul><li>Excellent customer service</li><li>A+ rating from the Trusted Trade Bureau</li></ul></div>
</div>
<div class="step" style="left:668px;top:2007px">
  <svg width="56" height="64" viewBox="0 0 56 64" aria-hidden="true"><path d="M18 4 H38 L32 14 H24 Z" fill="#1a6fc0"/><path d="M22 16 H34 C52 26 56 44 50 56 C46 62 10 62 6 56 C0 44 4 26 22 16 Z" fill="#1a6fc0"/><text x="28" y="52" text-anchor="middle" font-family="Lato, sans-serif" font-weight="700" font-size="26" fill="#fff">$</text></svg>
  <div><h3>SAVINGS</h3><ul><li>No fees to receive packages</li><li>No U.S. sales tax when using our New Hampshire warehouse</li><li>45 days free storage</li></ul></div>
</div>

<section class="tools">
  <h2 style="left:103px;top:56px">PACKING &amp; STORAGE</h2>
  <p class="tools-intro">Bringing you industry-specific expertise; whatever you're shipping, wherever you're shipping it.</p>
  <ul class="tools-list">
    <li>Shipper delivers a professional, efficient service</li>
    <li>Tailored to the specific needs of your business.</li>
    <li>Our services are designed around you.</li>
  </ul>

  <h2 style="left:633px;top:56px">CALCULATE SHIPPING</h2>
  <span class="field-label" style="left:637px;top:130px">Distance</span>
  <span class="radio" style="left:637px;top:154px"><i class="on"></i>Domestic</span>
  <span class="radio" style="left:730px;top:154px"><i></i>International</span>
  <span class="field-label" style="left:637px;top:186px">Weight</span>
  <div class="input" style="left:637px;top:207px;width:166px;height:31px"></div>
  <span class="field-label" style="left:637px;top:254px">Cargo Size</span>
  <div class="input" style="left:637px;top:276px;width:56px;height:31px">cm</div>
  <span class="field-label" style="left:707px;top:284px;color:#888">x</span>
  <div class="input" style="left:723px;top:276px;width:56px;height:31px">cm</div>
  <span class="field-label" style="left:637px;top:322px">Fragile</span>
  <div class="input" style="left:637px;top:344px;width:186px;height:31px;color:#555;justify-content:space-between">YES<span>&#9662;</span></div>

  <span class="field-label" style="left:910px;top:130px">Extra Services</span>
  <span class="radio" style="left:914px;top:154px"><i class="on"></i>Quick Delivery</span>
  <span class="radio" style="left:914px;top:176px"><i></i>Warranty</span>
  <span class="radio" style="left:914px;top:198px"><i></i>Gift Box</span>
  <p class="note">The Field below will show the double</p>
  <div class="input filled" style="left:910px;top:261px;width:166px;height:31px">$200</div>
  <div class="calc-btn">CALCULATE</div>
</section>

<section class="clients">
  <div class="clients-label"><span>OUR CLIENTS</span></div>
  <svg class="arrow" style="left:380px" width="22" height="34" viewBox="0 0 22 34" aria-hidden="true"><path d="M22 0 L0 17 L22 34 Z" fill="#111"/></svg>
  <span class="client" style="left:440px">Hollin</span>
  <span class="client" style="left:612px">Brightmart</span>
  <span class="client" style="left:818px">Rivora</span>
  <span class="client" style="left:962px">Bidlane</span>
  <svg class="arrow" style="left:1117px" width="22" height="34" viewBox="0 0 22 34" aria-hidden="true"><path d="M0 0 L22 17 L0 34 Z" fill="#111"/></svg>
</section>

<footer class="site-footer">
  <div class="footer-logo">
    <svg width="40" height="40" viewBox="0 0 40 40" aria-hidden="true"><circle cx="20" cy="20" r="17" fill="none" stroke="#fff" stroke-width="3"/><circle cx="20" cy="20" r="10" fill="#fff"/></svg>
    <span>Parvento</span>
  </div>
  <div class="footer-col" style="left:103px;top:104px">
    <a href="#">HOW IT WORKS</a><a href="#">PRICING</a><a href="#">TERMS OF SERVICE</a><a href="#">PRIVACY POLICY</a><a href="#">CONTACT US</a>
  </div>
  <div class="footer-col" style="left:339px">
    <h4>PARTNERSHIP WITH</h4>
    <p class="partner">Fastmoor</p><p class="partner">Kestrel Post</p><p class="partner">Northway Mail</p>
  </div>
  <div class="footer-col" style="left:646px">
    <h4>WORKING HOURS</h4>
    <p>9:00 AM TO 5:00 PM EST</p><p>WORKING DAYS:</p><p>MONDAY - FRIDAY</p><p>CURRENT TIME AT PARVENTO:</p><p>07:39:09 AM</p>
  </div>
  <div class="footer-col" style="left:925px">
    <h4>CONTACT US</h4>
    <p>ADDRESSS</p><p>FAX</p><p>1-555-491-0874</p><p>SUPPORT@PARVENTO.COM</p><p>CHATLINE</p>
  </div>
</footer>
<div class="bottom-bar">Copyright © 2017 , Parvento. All Rights Reserved.</div>

</body>
</html>
```